we can communicate on this, but i want to follow the approach we took on Pell|Quorn & Tillet but i feel the card front needs the black background and the platinum and gold logo. The back? I am open. we can use the same info from PQ&T. Vellum Crest is an enhanced equity investment fund - basically a very exclusive boutique hedge fund that uses only stock options. very advanced things. hope you are interested

Contact Information for Business Card

Dr. Owen T. Brisket, CFA
Scientifique de fusée financière
555.014.2296
TheDoc4793@mailvessel.example

4718 Fennel Brook Way N.
West Fargo, ND 58078

No web site

Colors

Designer to choose colors to be used in the design.

Requirements
Nice to have
• I tend to prefer the most visible applications of the logo to include logo and name, the logo version with a black background and the gold and platinum components separated by the black. I see this working well for a single side (logo and name - this is card front to me).
• I am fairly open to other treatments on the reverse side with the data. To me, it makes sense to have a different color rendition of the logo on the reverse and it may be a muted black tone on tone or an oversized portion that would have spot UV. Or, the reverse may play with colors and layout
Should not have
• Other colors = no no
• Decorative font

```html
<!DOCTYPE html>
<html lang="en">
<head>
<meta charset="utf-8">
<title>Vellum Crest — Business Card</title>
<link rel="stylesheet" href="https://fonts.googleapis.com/css2?family=Montserrat:wght@700&family=Open+Sans:wght@400&display=swap">
<style>
  :root {
    --backdrop: #e9e6e1;
    --card-light: #ffffff;
    --card-dark: #1b1b1b;
    --ink: #1a1a1a;
    --gold: #c39a22;
    --rule: #3a3a3a;
    --white: #ffffff;
  }
  * { margin: 0; padding: 0; box-sizing: border-box; }
  html, body {
    width: 1200px; height: 1000px; overflow: hidden;
    background: var(--backdrop);
  }
  .canvas { position: relative; width: 1200px; height: 1000px; }
  .card {
    position: absolute; width: 666px; height: 397px;
    box-shadow: 0 4px 10px rgba(0,0,0,0.25);
  }
  .card--info { left: 262px; top: 74px; background: var(--card-light); }
  .card--brand { left: 266px; top: 533px; background: var(--card-dark); }

  .brand-mark { position: absolute; border-radius: 50%; background: var(--gold); }
  .card--info .brand-mark { left: 453px; top: 34px; width: 104px; height: 104px; }
  .card--brand .brand-mark { left: 262px; top: 57px; width: 140px; height: 140px; }

  .brand-name {
    position: absolute;
    font-family: "Montserrat", sans-serif; font-weight: 700;
    letter-spacing: 0.02em; white-space: nowrap;
  }
  .card--info .brand-name {
    right: 43px; top: 160px; font-size: 31px; color: var(--ink); text-align: right;
  }
  .card--brand .brand-name {
    left: 0; right: 0; top: 245px; font-size: 44px; color: var(--white); text-align: center;
  }

  .holder-name {
    position: absolute; left: 45px; top: 241px;
    font-family: "Open Sans", sans-serif; font-size: 19px;
    color: var(--gold); letter-spacing: 0.01em;
  }
  .divider {
    position: absolute; left: 45px; top: 275px; width: 578px; height: 1.5px;
    background: var(--rule);
  }
  .contact {
    position: absolute; left: 45px; top: 290px; list-style: none;
    font-family: "Open Sans", sans-serif; font-size: 16px; line-height: 24.5px;
    color: var(--ink);
  }
</style>
</head>
<body>
  <main class="canvas">
    <section class="card card--info" aria-label="Card back with contact details">
      <div class="brand-mark" aria-hidden="true"></div>
      <div class="brand-name">VELLUM CREST</div>
      <div class="holder-name">GABRIEL THORNVALE</div>
      <div class="divider"></div>
      <ul class="contact">
        <li>(000)-000-0000</li>
        <li>info@vellumcrest.example</li>
        <li>42 Marrow Lane W., Halden, ON K0L 3X9</li>
      </ul>
    </section>

    <section class="card card--brand" aria-label="Card front with brand name">
      <div class="brand-mark" aria-hidden="true"></div>
      <div class="brand-name">VELLUM CREST</div>
    </section>
  </main>
</body>
</html>
```